5x5 Pop Up Display, Company Logo With Text and Graphics for Tradeshow Display

Design for a 5ft x 5ft pop up trade show display that will sit on top of a table. I usually prefer clean, somewhat minimalist designs. We are a food service company but it's not a requirement to have photos of food. Design elements should compliment the table cloth that we have for the booth. The below may be included depending on the design aesthetic.
Service Provided: Daily Meal Service, Kitchen Management
"Nationwide Footprint"
"Grassroots Service"
"Fresh Scratch Cooking"
"Custom Menus"
"Made To Order Meals"

```html
<!DOCTYPE html>
<html lang="en">
<head>
<meta charset="utf-8">
<title>Reed Roasting – Services</title>
<link href="https://fonts.googleapis.com/css2?family=Montserrat:wght@700;800&display=swap" rel="stylesheet">
<style>
  :root {
    --ink: #0a0a0a;
    --slate: #333437;
    --green: #86bd57;
    --green-dark: #6b8f55;
    --lime: #a9c04e;
    --orange: #f0592a;
    --amber: #f39a2a;
    --tan: #c68d5f;
    --gold: #dbbd4f;
    --sand: #e8c982;
    --stone-light: #f4f4f4;
    --stone-mid: #dcdcdc;
  }
  * { margin: 0; padding: 0; box-sizing: border-box; }
  html, body { width: 1200px; height: 1200px; overflow: hidden; }
  body { font-family: "Montserrat", Arial, sans-serif; }

  .display {
    position: relative;
    width: 1200px;
    height: 1200px;
    overflow: hidden;
    background:
      radial-gradient(ellipse at 85% 30%, rgba(150,150,150,.35), transparent 55%),
      radial-gradient(ellipse at 20% 45%, rgba(170,170,170,.3), transparent 50%),
      radial-gradient(ellipse at 50% 80%, rgba(255,255,255,.8), transparent 60%),
      linear-gradient(180deg, var(--stone-light), var(--stone-mid) 50%, var(--stone-light));
  }

  .brand {
    position: absolute;
    top: 58px;
    left: 0;
    width: 100%;
    text-align: center;
    font-weight: 800;
    color: var(--ink);
    text-transform: uppercase;
    line-height: .92;
  }
  .brand-line { display: block; }
  .brand-line--top { font-size: 118px; letter-spacing: 2px; }
  .brand-line--bottom { font-size: 112px; letter-spacing: 1px; }
  .brand-dot {
    display: inline-block;
    width: 26px; height: 26px;
    border-radius: 50%;
    background: var(--green);
    margin-left: 14px;
    vertical-align: 60px;
  }

  .services-title {
    position: absolute;
    top: 348px;
    left: 0;
    width: 100%;
    text-align: center;
    font-size: 72px;
    font-weight: 800;
    letter-spacing: 1px;
    background: linear-gradient(180deg, var(--green) 30%, var(--green-dark) 100%);
    -webkit-background-clip: text;
    background-clip: text;
    color: transparent;
  }

  .title-rule {
    position: absolute;
    top: 447px;
    left: 327px;
    width: 550px;
    height: 10px;
    display: flex;
  }
  .title-rule span { flex: 1; }

  .service-list {
    position: absolute;
    top: 537px;
    left: 193px;
    width: 840px;
    display: grid;
    grid-template-columns: 489px 1fr;
    row-gap: 46px;
    list-style: none;
  }
  .service {
    display: flex;
    align-items: stretch;
    font-size: 36px;
    font-weight: 800;
    line-height: 39px;
    text-transform: uppercase;
    color: var(--ink);
  }
  .service::before {
    content: "";
    width: 10px;
    margin-right: 12px;
    margin-top: 3px;
    background: var(--accent);
  }

  .tagline {
    position: absolute;
    top: 906px;
    left: 0;
    width: 100%;
    text-align: center;
    font-weight: 800;
    font-size: 51px;
    line-height: 52px;
    text-transform: uppercase;
  }
  .tagline-lead { display: block; color: var(--slate); }
  .tagline-em { display: block; color: var(--orange); }
  .tagline-rule {
    position: absolute;
    top: 1038px;
    left: 492px;
    width: 220px;
    height: 10px;
    background: var(--orange);
  }

  .base-wave { position: absolute; left: 0; top: 0; }
</style>
</head>
<body>
<main class="display">
  <h1 class="brand">
    <span class="brand-line brand-line--top">Reed<span class="brand-dot"></span></span>
    <span class="brand-line brand-line--bottom">Roasting</span>
  </h1>

  <h2 class="services-title">SERVICE ARE PROVIDED</h2>
  <div class="title-rule">
    <span style="background:var(--lime)"></span>
    <span style="background:var(--green)"></span>
    <span style="background:var(--tan)"></span>
    <span style="background:var(--gold)"></span>
  </div>

  <ul class="service-list">
    <li class="service" style="--accent:var(--lime)">Daily<br>Meal Service</li>
    <li class="service" style="--accent:var(--green)">Grassroots<br>Service</li>
    <li class="service" style="--accent:var(--green)">Kitchen<br>Management</li>
    <li class="service" style="--accent:var(--lime)">Fresh Scratch<br>Cooking</li>
    <li class="service" style="--accent:var(--orange)">Nationwide<br>Footprint</li>
    <li class="service" style="--accent:var(--amber)">Custom<br>Menus</li>
  </ul>

  <p class="tagline">
    <span class="tagline-lead">Made To</span>
    <span class="tagline-em">Order Meals</span>
  </p>
  <div class="tagline-rule"></div>

  <svg class="base-wave" width="1200" height="1200" viewBox="0 0 1200 1200" aria-hidden="true">
    <path d="M780 1185 C980 1180 1140 1100 1200 1000 L1200 1200 L780 1200 Z" fill="var(--sand)"/>
    <path d="M0 1112 C110 1075 200 1062 300 1066 C470 1072 600 1130 760 1163 C900 1192 1050 1188 1200 1160 L1200 1200 L0 1200 Z" fill="var(--green)"/>
  </svg>
</main>
</body>
</html>
```